Fundvane Informational Banners for Ashen Tide Rising

Hello, We are currently in the Process of doing a Fundvane Campaign which is due on the 4th. We need a Grungy/Dirty Dark Dead Feeling set of Banners, and Informational Pieces in Various Sizes.
Banner Sizes:
640px × 88px Normall Banner
640px × 57px Breaker Banner
700px × 93px Header Banner
640px × 635px Display Box for Rewards
A Larger box, that needs to have a Seamless beginning and ending also needs to be made, so it can be extended as more text and so-forth is completed.

We are looking for very Dead, Dark looking images, thesr are ment to be displayed on the fundvane webpage they need to flow well with the fundvane form, as well as show off our things, simple or advanced. They need to match our style.

NOTE IMPORTANT!!!!
THESE ARE NOT ADVERTISING BANNERS, THESE ARE BANNERS FOR THE FUNDVANE WEBSITE FOR A CAMPAIGN PLEASE DO SOME HOMEWORK BEFORE ATTEMPTING THESE IMAGES WE ARE NOT LOOKING FOR ADVERTISING BANNERS WE ARE LOOKING FOR INFORMATIONAL PIECES

Example of words that will be used on the various Banners

"Physical Add-ons"
"Digital Add-ons"
"Who we are"
"What is Ashen Tide Rising?"
"What is Procedural Generation?"
"Why are you Attempting this?"

THESE ARE EXAMPLE SENTENCES THAT WILL BE IN THE BANNERS I REPEAT THESE ARE NOT ADVERTISING WEBBANNERS
Updates

Everyone is Doing wonderful, thank you all for making such lovely work. thank You. Keep it up, remember undead feel, it must be functional piece on the fundvane website. :3 

Target Market(s)

Zombie, and Undead ages People 13-51 that are Gamers

Industry/Entity Type

Digital

Requirements
Must have
• These Designs must be Boxes and Banners, and Break Points for a Fundvane Information Display I will provide a few links here.
http://www.fundvane-example.com/projects/brevmoor/harrow-veils-of-quillan
http://www.fundvane-example.com/projects/corvale/venture-paragon

Our Artwork Style & Concept Artwork can be found here
http://www.gamevault-example.net/games/ashen-tide-rising/images

```html
<!DOCTYPE html>
<html lang="en">
<head>
<meta charset="utf-8">
<title>Ashen Tide Rising – Section Banner</title>
<link rel="stylesheet" href="https://fonts.googleapis.com/css2?family=Special+Elite&display=swap">
<style>
  :root {
    --page-bg: #666b6e;
    --banner-deep: #07121c;
    --banner-mid: #14324a;
    --banner-glow: #3d6f86;
    --banner-haze: #9fc4d2;
    --title-ink: #f1e6e4;
    --title-shadow: #1a0f10;
  }
  html, body {
    margin: 0;
    padding: 0;
    width: 1200px;
    height: 600px;
    overflow: hidden;
    background: var(--page-bg);
  }
  .canvas {
    position: relative;
    width: 1200px;
    height: 600px;
  }
  .section-banner {
    position: absolute;
    left: 75px;
    top: 230px;
    width: 1050px;
    height: 139px;
    overflow: hidden;
  }
  .banner-backdrop {
    position: absolute;
    inset: 0;
    background:
      radial-gradient(ellipse 180px 40px at 380px 10px, rgba(159,196,210,0.75), transparent 70%),
      radial-gradient(ellipse 260px 60px at 620px 120px, rgba(61,111,134,0.55), transparent 75%),
      radial-gradient(ellipse 220px 70px at 250px 80px, rgba(20,50,74,0.9), transparent 80%),
      linear-gradient(100deg, var(--banner-deep) 0%, var(--banner-mid) 35%, var(--banner-deep) 60%, var(--banner-mid) 80%, var(--banner-deep) 100%);
  }
  .banner-title {
    position: absolute;
    inset: 0;
    margin: 0;
    display: flex;
    align-items: center;
    justify-content: center;
    font-family: "Special Elite", "Courier New", monospace;
    font-weight: 400;
    font-size: 60px;
    color: var(--title-ink);
    text-shadow: 2px 3px 3px var(--title-shadow), 0 0 1px var(--title-ink);
    -webkit-text-stroke: 1px var(--title-ink);
    white-space: nowrap;
  }
</style>
</head>
<body>
  <main class="canvas">
    <section class="section-banner">
      <div class="banner-backdrop" role="img" aria-label="Dark blue grunge artwork of a ruined, shadowy scene"></div>
      <h1 class="banner-title">Why are you Attempting this?</h1>
    </section>
  </main>
</body>
</html>
```